Facebook post for announcing the new company's website design

Need a facebook post (English language) for announcing that the company has a renovated website:
https://www.clinivostaremoto.com/en/

The website existed already but received recently a brand new design: more light, modern and sophisticated.

Please find as an attachment source files of our logo so that you can provide the best quality, thanks.

Also you may find our facebook page at:
https://pt-pt.facebook.com/clinivostaremoto/

Target Market(s)

Facebook audience

Colors

Designer to choose colors to be used in the design.

Requirements
Must have
• Our website has a new design!
• www.clinivostaremoto.com
Nice to have
• The post should feel as somehow connected to the website. Please check our above mentioned website, things should be related. For instance, use our logo (check attached files).
• You may also use this opportunity to remind the audience about our business core messages: excellency, quality, safety.

```html
<!DOCTYPE html>
<html lang="en">
<head>
<meta charset="utf-8">
<title>Clinivosta Remoto – New Website Post</title>
<link rel="stylesheet" href="https://fonts.googleapis.com/css2?family=Montserrat:wght@500;700;800&family=Arimo:wght@400&display=swap">
<style>
  :root {
    --brand-blue: #1e9fd0;
    --brand-blue-deep: #1a8fc2;
    --band-navy: #0e6e9c;
    --text-grey: #4a4a4a;
    --sub-grey: #8a8a8a;
    --accent-orange: #e8862a;
    --white: #ffffff;
  }
  * { box-sizing: border-box; margin: 0; padding: 0; }
  html, body { width: 1200px; height: 1200px; overflow: hidden; background: var(--white); }
  .post { position: relative; width: 1200px; height: 1200px; background: var(--white); font-family: "Montserrat", sans-serif; }

  .team-photo {
    position: absolute; left: 0; top: 0; width: 1200px; height: 658px;
    background:
      radial-gradient(ellipse 60% 70% at 50% 75%, #f3f5f7 0%, rgba(243,245,247,0) 70%),
      linear-gradient(90deg, #4fc7c4 0%, #2f86d0 28%, #f2f4f6 50%, #2c7fcf 70%, #8fb4e3 90%, #e9eef2 100%);
  }
  .team-photo::before {
    content: ""; position: absolute; inset: 0;
    background: linear-gradient(180deg, #eef2f5 0%, rgba(238,242,245,0.85) 30%, rgba(238,242,245,0) 60%);
  }

  .shapes { position: absolute; left: 0; top: 0; width: 1200px; height: 1200px; }

  .brand { position: absolute; left: 66px; top: 680px; display: flex; align-items: center; gap: 16px; }
  .brand-mark { width: 78px; height: 78px; background: var(--brand-blue-deep); }
  .brand-name { font-weight: 800; font-size: 40px; line-height: 40px; color: var(--brand-blue-deep); letter-spacing: 0.5px; }
  .brand-tagline { position: absolute; left: 168px; top: 760px; font-family: "Arimo", sans-serif; font-size: 17px; color: var(--sub-grey); white-space: nowrap; }

  .section-pill {
    position: absolute; left: 66px; height: 35px; padding: 0 12px;
    border: 2px solid var(--brand-blue-deep); border-radius: 18px;
    font-weight: 700; font-size: 19px; line-height: 31px; color: var(--brand-blue-deep); white-space: nowrap;
  }
  .pill-provide { top: 802px; }
  .pill-advantages { top: 1000px; }

  .check-list { position: absolute; left: 66px; list-style: none; }
  .check-list li { display: flex; align-items: center; gap: 8px; height: 26px; font-weight: 500; font-size: 20px; color: var(--text-grey); white-space: nowrap; }
  .check-list svg { width: 18px; height: 18px; flex: none; }
  .list-provide { top: 852px; }
  .list-advantages { top: 1044px; }

  .contact { position: absolute; left: 300px; width: 330px; top: 1118px; text-align: center; font-family: "Arimo", sans-serif; font-size: 20px; color: var(--white); }
  .contact p { display: flex; align-items: center; justify-content: center; gap: 8px; height: 30px; }
  .contact svg { width: 18px; height: 18px; }

  .announcement { position: absolute; left: 700px; width: 475px; top: 686px; text-align: center; font-weight: 700; font-size: 28px; line-height: 34px; color: var(--white); white-space: nowrap; }

  .headline { position: absolute; left: 700px; width: 475px; top: 736px; text-align: center; font-weight: 800; font-size: 72px; line-height: 72px; color: var(--white); }

  .cta { position: absolute; left: 768px; top: 1050px; width: 334px; height: 61px; border-radius: 31px; background: var(--accent-orange); color: var(--white); font-weight: 700; font-size: 31px; line-height: 61px; text-align: center; letter-spacing: 0.5px; }

  .web { position: absolute; left: 690px; width: 490px; top: 1145px; text-align: center; font-family: "Arimo", sans-serif; font-size: 25px; color: var(--white); }
</style>
</head>
<body>
<div class="post">
  <div class="team-photo" role="img" aria-label="Photo of five smiling medical professionals in scrubs and a white coat with stethoscopes, standing in a bright clinic"></div>

  <svg class="shapes" viewBox="0 0 1200 1200" aria-hidden="true">
    <polygon points="275,1104 638,1104 675,1200 229,1200" fill="var(--band-navy)"/>
    <polygon points="669,658 686,658 575,932 681,1200 664,1200 559,932" fill="var(--brand-blue)"/>
    <polygon points="698,658 1200,658 1200,1200 698,1200 589,932" fill="var(--brand-blue)"/>
  </svg>

  <div class="brand">
    <div class="brand-mark"></div>
    <div class="brand-name">CLINIVOSTA<br>REMOTO</div>
  </div>
  <div class="brand-tagline">Professor Doutor Rui Almeida Tavares</div>

  <div class="section-pill pill-provide">WE PROVIDE</div>
  <ul class="check-list list-provide">
    <li><svg viewBox="0 0 18 18"><path d="M2 10 L7 15 L16 3" fill="none" stroke="#1a8fc2" stroke-width="2.5"/></svg>Intervention by top specialists</li>
    <li><svg viewBox="0 0 18 18"><path d="M2 10 L7 15 L16 3" fill="none" stroke="#1a8fc2" stroke-width="2.5"/></svg>Sub-specialised analysis of all exams</li>
    <li><svg viewBox="0 0 18 18"><path d="M2 10 L7 15 L16 3" fill="none" stroke="#1a8fc2" stroke-width="2.5"/></svg>Filling-in occasional or permanent needs</li>
    <li><svg viewBox="0 0 18 18"><path d="M2 10 L7 15 L16 3" fill="none" stroke="#1a8fc2" stroke-width="2.5"/></svg>Day coverage</li>
    <li><svg viewBox="0 0 18 18"><path d="M2 10 L7 15 L16 3" fill="none" stroke="#1a8fc2" stroke-width="2.5"/></svg>International scope</li>
  </ul>

  <div class="section-pill pill-advantages">OUR ADVANTAGES</div>
  <ul class="check-list list-advantages">
    <li><svg viewBox="0 0 18 18"><path d="M2 10 L7 15 L16 3" fill="none" stroke="#1a8fc2" stroke-width="2.5"/></svg>Controlled costs</li>
    <li><svg viewBox="0 0 18 18"><path d="M2 10 L7 15 L16 3" fill="none" stroke="#1a8fc2" stroke-width="2.5"/></svg>Excellency</li>
    <li><svg viewBox="0 0 18 18"><path d="M2 10 L7 15 L16 3" fill="none" stroke="#1a8fc2" stroke-width="2.5"/></svg>Safety</li>
    <li><svg viewBox="0 0 18 18"><path d="M2 10 L7 15 L16 3" fill="none" stroke="#1a8fc2" stroke-width="2.5"/></svg>Speediness</li>
    <li><svg viewBox="0 0 18 18"><path d="M2 10 L7 15 L16 3" fill="none" stroke="#1a8fc2" stroke-width="2.5"/></svg>Quality</li>
  </ul>

  <div class="contact">
    <p><svg viewBox="0 0 18 18"><path d="M4 2 L7 2 L8 6 L6 7.5 C7 10 8 11 10.5 12 L12 10 L16 11 L16 14 C16 15 15 16 14 16 C8 15.5 2.5 10 2 4 C2 3 3 2 4 2 Z" fill="#e8862a"/></svg>+351 900 123 456</p>
    <p><svg viewBox="0 0 18 18"><rect x="1" y="4" width="16" height="11" fill="#e8862a"/><path d="M1 4 L9 10 L17 4" fill="none" stroke="#0e6e9c" stroke-width="1.5"/></svg>info@clinivostaremoto.com</p>
  </div>

  <p class="announcement">Our website has a new design!</p>

  <h1 class="headline">YOUR ONE<br>STOP<br>MEDICAL<br>SOLUTION</h1>

  <div class="cta">VISIT US NOW</div>

  <div class="web">www.clinivostaremoto.com/en</div>
</div>
</body>
</html>
```